Orthopedic Arm Surgeon Brochure

Bifold modern design. I will supply the text, my photo, and photos of my textbooks. Prefer colors in the greens, blues, greys. For more information visit LimbForwardClinic.com Please feel free to e-mail me with any questions. Current brochure attached; I want to modernize this, get rid of frames, and change the text.

Target Market(s)

High-end market

Colors
3176b5
33a6d7
33b8a4
abd036
876aae
b768aa

Requirements
Must have
• Beautiful finishes
Should not have
• Bright reds, yellows, oranges that emit fear

```html
<!DOCTYPE html>
<html lang="en">
<head>
<meta charset="utf-8">
<title>Limb Forward Clinic – Bifold Brochure</title>
<link href="https://fonts.googleapis.com/css2?family=Montserrat:wght@500;700;800&family=Open+Sans:wght@400;600&display=swap" rel="stylesheet">
<style>
  :root{
    --bg:#e3e4e4;
    --blue:#3176b5;
    --blue-dark:#1f5b94;
    --sky:#33a6d7;
    --teal:#33b8a4;
    --lime:#abd036;
    --ink:#3b4450;
    --muted:#7a8490;
    --paper:#ffffff;
  }
  *{box-sizing:border-box;margin:0;padding:0}
  html,body{width:898px;height:1200px;overflow:hidden;background:var(--bg)}
  body{font-family:"Open Sans",Arial,sans-serif;color:var(--ink)}
  .spread{position:absolute;left:49px;width:800px;height:520px;display:flex;box-shadow:0 6px 18px rgba(0,0,0,.18);background:var(--paper)}
  .spread--outside{top:40px}
  .spread--inside{top:640px}
  .panel{position:relative;width:400px;height:520px;overflow:hidden}
  .panel + .panel{border-left:1px solid #e6e8ea}
  .layer{position:absolute;inset:0}

  /* brand */
  .brand{position:absolute;top:22px;left:150px;display:flex;align-items:center;gap:7px;font-family:"Montserrat",Arial,sans-serif;font-weight:800;font-size:13px;color:var(--blue);letter-spacing:.5px;text-transform:uppercase}
  .brand__dot{width:14px;height:14px;border-radius:50%;background:var(--teal)}
  .tagline{position:absolute;top:48px;left:172px;width:200px;font-size:9px;line-height:1.45;color:var(--muted)}

  /* back panel */
  .photo{position:absolute}
  .photo--doctor{left:22px;top:72px;width:140px;height:150px;background:linear-gradient(160deg,#6c6f76,#2b2f38)}
  .photo--books{left:190px;top:120px;width:188px;height:118px;background:linear-gradient(120deg,#8a3c49,#3f5f8a 55%,#c7b48a)}
  .name-tag{position:absolute;left:70px;top:210px;padding:5px 14px;background:var(--lime);font-family:"Montserrat",Arial,sans-serif;font-weight:700;font-size:11px;color:var(--paper);letter-spacing:1px}
  .conditions{position:absolute;left:22px;top:300px;width:356px;color:var(--paper)}
  .conditions__title{font-family:"Montserrat",Arial,sans-serif;font-weight:700;font-size:14px;line-height:1.3;margin-bottom:12px}
  .conditions__lists{display:flex;gap:24px}
  .conditions ul{list-style:none;font-size:10.5px;line-height:1.9}
  .conditions li::before{content:"";display:inline-block;width:6px;height:6px;margin-right:7px;background:var(--lime);border-radius:50%;vertical-align:middle}

  /* front panel */
  .photo--shoulder{left:0;top:0;width:400px;height:300px;background:radial-gradient(circle at 62% 30%,#d98b7c 0,#e9c3aa 30%,#f1ddd0 60%,#e8eef2 100%)}
  .front-brand{position:absolute;top:18px;left:20px;display:flex;align-items:center;gap:6px;font-family:"Montserrat",Arial,sans-serif;font-weight:800;font-size:11px;color:var(--blue);text-transform:uppercase}
  .front-brand__dot{width:11px;height:11px;border-radius:50%;background:var(--teal)}
  .headline{position:absolute;left:24px;top:346px;width:352px;color:var(--paper)}
  .headline__lead{font-size:11px;line-height:1.5;text-transform:uppercase;letter-spacing:.5px}
  .headline__main{font-family:"Montserrat",Arial,sans-serif;font-weight:800;font-size:20px;line-height:1.15;margin-top:6px;text-transform:uppercase}
  .contact-bar{position:absolute;left:0;bottom:26px;width:400px;height:40px;background:var(--teal);display:flex;align-items:center;gap:14px;padding-left:24px;color:var(--paper)}
  .contact-bar__phone{font-family:"Montserrat",Arial,sans-serif;font-weight:800;font-size:17px}
  .contact-bar__web{font-size:10px;font-weight:600}

  /* inside */
  .page{padding:28px 26px 0}
  .section-head{display:inline-block;background:var(--blue);color:var(--paper);font-family:"Montserrat",Arial,sans-serif;font-weight:700;font-size:10.5px;padding:4px 12px;margin:10px 0 7px;border-left:4px solid var(--lime)}
  .page p{font-size:9.5px;line-height:1.6;color:var(--ink)}
  .inside-band{position:absolute;left:0;bottom:0;width:400px;height:100px}
  .inside-web{position:absolute;left:24px;bottom:18px;font-size:10px;font-weight:600;color:var(--paper)}
  .circle-photo{position:absolute;bottom:14px;width:64px;height:64px;border-radius:50%;border:3px solid var(--paper)}
  .circle-photo--xray{left:160px;background:radial-gradient(circle,#f0a3a0,#6d7fb8 70%)}
  .circle-photo--hand{right:30px;background:radial-gradient(circle,#eac9b5,#8fb7d8 75%)}
</style>
</head>
<body>

<!-- outside spread -->
<section class="spread spread--outside">
  <article class="panel panel--back">
    <svg class="layer" viewBox="0 0 400 520" preserveAspectRatio="none" aria-hidden="true">
      <polygon points="0,0 130,0 60,60 0,60" fill="#33b8a4"/>
      <polygon points="0,270 400,240 400,520 0,520" fill="#3176b5"/>
      <polygon points="0,255 400,228 400,240 0,270" fill="#33a6d7"/>
      <polygon points="0,470 400,490 400,520 0,520" fill="#1f5b94"/>
    </svg>
    <div class="brand"><span class="brand__dot"></span>Limb Forward Clinic</div>
    <p class="tagline">Restoring motion, strength and confidence for every patient.</p>
    <div class="photo photo--doctor" role="img" aria-label="Portrait photo of the surgeon in a dark suit"></div>
    <div class="photo photo--books" role="img" aria-label="Photo of the surgeon's published textbooks"></div>
    <div class="name-tag">DR. HALDEN</div>
    <div class="conditions">
      <h2 class="conditions__title">Dr. Halden Uses Powers In The Following Conditions</h2>
      <div class="conditions__lists">
        <ul><li>Shoulder arthroscopy</li><li>Rotator cuff repair</li><li>Elbow reconstruction</li></ul>
        <ul><li>Wrist fractures</li><li>Carpal tunnel release</li><li>Nerve compression</li></ul>
      </div>
    </div>
  </article>

  <article class="panel panel--front">
    <div class="photo photo--shoulder" role="img" aria-label="Photo of a patient holding a painful shoulder"></div>
    <div class="front-brand"><span class="front-brand__dot"></span>Limb Forward Clinic</div>
    <svg class="layer" viewBox="0 0 400 520" preserveAspectRatio="none" aria-hidden="true">
      <polygon points="0,310 400,280 400,520 0,520" fill="#3176b5"/>
      <polygon points="0,296 400,266 400,280 0,310" fill="#33a6d7"/>
      <rect x="0" y="494" width="400" height="26" fill="#1f5b94"/>
    </svg>
    <div class="headline">
      <p class="headline__lead">Expert care for your<br>shoulder, elbow, wrist &amp; hand</p>
      <h1 class="headline__main">Board Certified<br>Orthopedic Surgeon</h1>
    </div>
    <div class="contact-bar">
      <span class="contact-bar__phone">555-014-2291</span>
      <span class="contact-bar__web">LimbForwardClinic.com</span>
    </div>
  </article>
</section>

<!-- inside spread -->
<section class="spread spread--inside">
  <article class="panel page">
    <span class="section-head">About Dr. Halden</span>
    <p>Dr. Halden is a board certified orthopedic surgeon focused on the upper limb. He treats injuries of the shoulder, elbow, wrist and hand with modern techniques and careful planning.</p>
    <span class="section-head">Our Approach</span>
    <p>Every plan begins with listening. We explain each option clearly, combine surgery with therapy when needed, and follow every patient until full function returns.</p>
    <svg class="inside-band" viewBox="0 0 400 100" preserveAspectRatio="none" aria-hidden="true">
      <polygon points="0,30 400,50 400,100 0,100" fill="#3176b5"/>
      <polygon points="0,20 400,42 400,50 0,30" fill="#33b8a4"/>
    </svg>
    <span class="inside-web">LimbForwardClinic.com</span>
    <div class="circle-photo circle-photo--xray" role="img" aria-label="Medical image of an injured joint"></div>
  </article>

  <article class="panel page">
    <span class="section-head">Conditions Treated</span>
    <p>Common conditions include rotator cuff tears, tennis elbow, fractures, arthritis and nerve compression. Many respond well to minimally invasive care and a short recovery.</p>
    <span class="section-head">Published Author</span>
    <p>Dr. Halden has written several textbooks used by surgeons in training across the country.</p>
    <span class="section-head">Visit Us</span>
    <p>For more information visit LimbForwardClinic.com. Please feel free to e-mail me with any questions.</p>
    <svg class="inside-band" viewBox="0 0 400 100" preserveAspectRatio="none" aria-hidden="true">
      <polygon points="0,50 400,30 400,100 0,100" fill="#3176b5"/>
      <polygon points="0,42 400,20 400,30 0,50" fill="#33b8a4"/>
    </svg>
    <div class="circle-photo circle-photo--hand" role="img" aria-label="Photo of a hand being examined"></div>
  </article>
</section>

</body>
</html>
```